Email Banner - TamberFold.com

I need an email banner created for my website: Tamberfold.com.
The logos are attatched here and an example of an email banner we have used in the past is also attatched. Please keep the tagline: "Essential Whitepapers for Business Professionals" - The logos are in the marvotta zip folder.

Logo Text

Tamberfold

```html
<!DOCTYPE html>
<html lang="en">
<head>
<meta charset="utf-8">
<title>Tamberfold Email Banner</title>
<link rel="stylesheet" href="https://fonts.googleapis.com/css2?family=Montserrat:wght@300;400;700&display=swap">
<style>
  :root {
    --navy: #243180;
    --sky: #89a9fe;
    --bright: #3a6ffb;
    --white: #ffffff;
    --page: #fefefe;
  }
  html, body {
    margin: 0;
    padding: 0;
    width: 1200px;
    height: 1000px;
    overflow: hidden;
    background: var(--page);
    font-family: "Montserrat", Arial, sans-serif;
  }
  .banner {
    position: absolute;
    left: 195px;
    top: 430px;
    width: 810px;
    height: 127px;
    background: var(--navy);
    overflow: hidden;
  }
  .banner-shapes {
    position: absolute;
    inset: 0;
    width: 810px;
    height: 127px;
  }
  .brand-name {
    position: absolute;
    left: 120px;
    width: 0;
    top: 0;
    height: 127px;
    display: flex;
    align-items: center;
    justify-content: center;
    margin-left: 0;
  }
  .brand-name span {
    position: absolute;
    left: 0;
    transform: translateX(-50%);
    white-space: nowrap;
    color: var(--white);
    font-weight: 700;
    font-size: 21px;
    letter-spacing: -0.3px;
  }
  .tagline {
    position: absolute;
    margin: 0;
    color: var(--white);
    font-weight: 300;
    line-height: 1;
    white-space: nowrap;
  }
  .tagline-top {
    left: 286px;
    top: 34px;
    font-size: 28px;
    letter-spacing: 0.6px;
  }
  .tagline-bottom {
    left: 327px;
    top: 61px;
    font-size: 28px;
  }
  .tagline-bottom .connector {
    font-size: 23px;
    margin-right: 9px;
    letter-spacing: 0.4px;
  }
  .tagline-bottom strong {
    font-weight: 700;
    letter-spacing: 0.4px;
  }
  .cta {
    position: absolute;
    left: 716px;
    top: 10px;
    color: var(--white);
    font-weight: 700;
    font-size: 11.5px;
    letter-spacing: 0.1px;
    text-decoration: none;
  }
</style>
</head>
<body>
  <section class="banner" aria-label="Tamberfold email banner">
    <svg class="banner-shapes" viewBox="0 0 810 127" aria-hidden="true">
      <path fill="var(--bright)" d="M118,0 H810 V117.5 L348,118 C288,118 267,97 237,57 C212,22 198,1 123,1 Z"/>
      <path fill="var(--sky)" d="M125,0 H810 V115 L350,116 C290,116 270,95 240,55 C215,20 200,0 125,0 Z"/>
      <path fill="var(--bright)" d="M670,0 H810 V44 C805,34 795,31 785,31 H720 C705,31 700,22 694,12 C688,3 682,0 670,0 Z"/>
    </svg>

    <div class="brand-name"><span>Tamberfold</span></div>

    <p class="tagline tagline-top">Essential Whitepapers</p>
    <p class="tagline tagline-bottom"><span class="connector">for</span><strong>Business Professionals</strong></p>

    <a class="cta" href="#">CLICK HERE</a>
  </section>
</body>
</html>
```